Personal creative Biz Card Design

Need personal yet natural and organic design. The cards I have now are well designed but look too commercial. I want more organic FEELING kind of card. I thought having a headshot would make it more personal... but maybe a sketch effect (or line drawing effect) of face better (?). Maybe in a gray or tungsten color?

Target Market(s)

Well, everyone i give card to will have already seen me face-to-face so that is one thing. Mostly yoga students and people interested in improving their fitness or general health. People looking for wellness, a personal fitness trainer, a yoga teacher

Industry/Entity Type

Health And Wellness

Contact Information for Business Card

I provided examples

Requirements
Must have
• My main logo
• My name

```html
<!DOCTYPE html>
<html lang="en">
<head>
<meta charset="utf-8">
<title>Leo Marsh – Business Cards</title>
<link rel="stylesheet" href="https://fonts.googleapis.com/css2?family=Varela+Round&family=Lora:wght@400;500&display=swap">
<style>
  :root {
    --stage-light: #eceded;
    --stage-dark: #cfd0d2;
    --leaf-green: #8dc63f;
    --name-green: #6a9a3a;
    --ink-gray: #5a5a5a;
    --card-white: #ffffff;
    --card-black: #000000;
    --steel-dark: #4a4a4c;
    --steel-light: #b9babc;
    --band-green: #5f8a2a;
    --band-steel: #8e8f92;
  }
  html, body {
    margin: 0;
    width: 1200px;
    height: 900px;
    overflow: hidden;
  }
  body {
    background: radial-gradient(ellipse at 45% 40%, var(--stage-light), var(--stage-dark));
  }
  .sheet { display: block; }
  .name { font-family: "Varela Round", sans-serif; font-size: 28px; font-weight: 700; }
  .tagline { font-family: "Varela Round", sans-serif; font-size: 9.5px; fill: var(--ink-gray); }
  .phone { font-family: "Varela Round", sans-serif; font-size: 13px; letter-spacing: 2px; }
  .web { font-family: "Lora", serif; letter-spacing: 3px; }
  .mail { font-family: "Varela Round", sans-serif; letter-spacing: 2px; }
  .back-name { font-family: "Varela Round", sans-serif; font-size: 26px; letter-spacing: 3px; fill: var(--card-white); }
</style>
</head>
<body>
<svg class="sheet" width="1200" height="900" viewBox="0 0 1200 900" xmlns="http://www.w3.org/2000/svg">
  <defs>
    <linearGradient id="steel-sweep" x1="0" y1="0" x2="1" y2="0">
      <stop offset="0" stop-color="var(--steel-dark)"/>
      <stop offset="0.45" stop-color="var(--steel-light)"/>
      <stop offset="1" stop-color="var(--steel-dark)"/>
    </linearGradient>
  </defs>

  <!-- Front, green -->
  <g class="card card-front card-green" transform="translate(85 107)">
    <rect width="470" height="272" fill="var(--card-white)"/>
    <path d="M470,8 C455,120 300,212 0,222 L0,272 L470,272 Z" fill="var(--leaf-green)"/>
    <rect x="0" y="214" width="230" height="8" fill="var(--leaf-green)" opacity="0.55" role="img" aria-label="Row of small diamonds along the curve"/>
    <circle cx="330" cy="14" r="7" fill="var(--ink-gray)"/>
    <rect x="327" y="9" width="6" height="10" rx="1" fill="var(--card-white)"/>
    <text class="phone" x="347" y="19" fill="var(--leaf-green)">555-203-4187</text>
    <circle cx="42" cy="72" r="26" fill="var(--leaf-green)"/>
    <text class="name" x="72" y="76" fill="var(--name-green)">LEO MARSH</text>
    <text class="tagline" x="60" y="96">Steady Support for a Balanced Living</text>
    <text class="web" x="250" y="242" font-size="17" fill="var(--card-white)" text-anchor="middle">www.leomarsh.com</text>
    <text class="mail" x="250" y="262" font-size="14" fill="var(--card-white)" text-anchor="middle">leoinnerpaths@mail.com</text>
  </g>

  <!-- Back, green -->
  <g class="card card-back card-green" transform="translate(638 112)">
    <rect width="470" height="270" fill="var(--leaf-green)"/>
    <rect y="198" width="470" height="72" fill="var(--card-black)"/>
    <rect y="186" width="470" height="12" fill="var(--band-green)" role="img" aria-label="Row of diamonds dividing the card"/>
    <text class="back-name" x="235" y="112" text-anchor="middle">LEO MARSH</text>
    <text class="web" x="235" y="227" font-size="15" fill="var(--leaf-green)" text-anchor="middle">www.leomarsh.com</text>
    <text class="mail" x="235" y="247" font-size="12" fill="var(--leaf-green)" text-anchor="middle">leoinnerpaths@mail.com</text>
  </g>

  <!-- Front, steel -->
  <g class="card card-front card-steel" transform="translate(85 450)">
    <rect width="470" height="271" fill="var(--card-white)"/>
    <path d="M470,8 C455,120 300,212 0,222 L0,271 L470,271 Z" fill="url(#steel-sweep)"/>
    <rect x="0" y="214" width="230" height="8" fill="var(--steel-light)" opacity="0.7" role="img" aria-label="Row of small diamonds along the curve"/>
    <circle cx="330" cy="14" r="7" fill="var(--ink-gray)"/>
    <rect x="327" y="9" width="6" height="10" rx="1" fill="var(--card-white)"/>
    <text class="phone" x="347" y="19" fill="var(--ink-gray)">555-203-4187</text>
    <circle cx="42" cy="72" r="26" fill="var(--leaf-green)"/>
    <text class="name" x="72" y="76" fill="var(--name-green)">LEO MARSH</text>
    <text class="tagline" x="60" y="96">Steady Support for a Balanced Living</text>
    <text class="web" x="250" y="242" font-size="17" fill="var(--card-white)" text-anchor="middle">www.leomarsh.com</text>
    <text class="mail" x="250" y="262" font-size="14" fill="var(--card-white)" text-anchor="middle">leoinnerpaths@mail.com</text>
  </g>

  <!-- Back, steel -->
  <g class="card card-back card-steel" transform="translate(638 454)">
    <rect width="470" height="271" fill="url(#steel-sweep)"/>
    <rect y="206" width="470" height="65" fill="var(--card-black)"/>
    <rect y="194" width="470" height="12" fill="var(--band-steel)" role="img" aria-label="Row of diamonds dividing the card"/>
    <text class="back-name" x="235" y="112" text-anchor="middle">LEO MARSH</text>
    <text class="web" x="235" y="232" font-size="15" fill="var(--card-white)" text-anchor="middle">www.leomarsh.com</text>
    <text class="mail" x="235" y="252" font-size="12" fill="var(--card-white)" text-anchor="middle">leoinnerpaths@mail.com</text>
  </g>
</svg>
</body>
</html>
```